Home Improvements Website

I would like a website that matches our business colour scheme and uses the fonts consistent without logo. (Monserrat, Chosence & Big Noddle Tiling).
We will need numerous sections: homepage, about us, services (with tiles or links to each service - building, landscaping, decking, maintenance, roofing, gutters etc) current projects (which must be easily editable by me, who is not too tech savvy) and a contacts page with enquiry form we can link to our job management service (Tradify).

```html
<!DOCTYPE html>
<html lang="en">
<head>
<meta charset="utf-8">
<title>Harrowmere – Home Improvements</title>
<link rel="stylesheet" href="https://fonts.googleapis.com/css2?family=Cabin:wght@700&family=IBM+Plex+Sans:wght@600;700&family=Poppins:wght@300;400;500;600&display=swap">
<style>
:root{
  --green:#14892f;
  --green-dark:#0a6a22;
  --green-light:#8cc63f;
  --charcoal:#2b3330;
  --charcoal-2:#323a37;
  --bronze:#a3804a;
  --bronze-dark:#8a6a38;
  --ink:#1e1e1e;
  --body:#444;
  --muted:#777;
  --field:#ececec;
  --paper:#f6f6f6;
  --white:#fff;
  --head:"IBM Plex Sans",Arial,sans-serif;
  --display:"Cabin",Arial,sans-serif;
  --text:"Poppins",Arial,sans-serif;
}
*{box-sizing:border-box;margin:0;padding:0}
html,body{width:1200px;height:5051px;overflow:hidden}
body{position:relative;font-family:var(--text);color:var(--body);background:var(--white)}
.abs{position:absolute}
a{color:inherit;text-decoration:none}

/* top bar */
.topbar{left:0;top:0;width:1200px;height:40px;background:var(--charcoal);color:#fff;font-size:13px}
.topbar .social{position:absolute;top:13px;width:14px;height:14px;border-radius:50%;border:1.5px solid #fff}
.topbar .phone{position:absolute;left:236px;top:10px;display:flex;gap:7px;align-items:center}
.topbar .mail{position:absolute;right:106px;top:10px;display:flex;gap:7px;align-items:center}

/* nav */
.nav{left:0;top:40px;width:1200px;height:58px;background:#fff;box-shadow:0 2px 6px rgba(0,0,0,.08);font-size:14px;color:#333}
.nav a{position:absolute;top:19px}
.nav .active{color:var(--green)}
.nav .sep{position:absolute;top:0;width:1px;height:58px;background:#e3e3e3}
.nav .quote{position:absolute;left:953px;top:0;width:143px;height:58px;background:var(--green);color:#fff;display:flex;align-items:center;justify-content:center;gap:7px}
.brand-badge{left:533px;top:0;width:134px;height:137px;background:#fff;border-radius:0 0 60px 60px;box-shadow:0 4px 10px rgba(0,0,0,.15);display:flex;align-items:center;justify-content:center;gap:6px}
.brand-name{font-family:var(--text);font-weight:600;font-size:15px;color:var(--charcoal);letter-spacing:.5px}
.brand-dot{width:10px;height:10px;background:var(--green)}

/* hero */
.hero{left:0;top:98px;width:1200px;height:702px;background:linear-gradient(180deg,#6f9ccc 0%,#a9c4dc 22%,#4e5756 45%,#3f4a3f 60%,#4f8a2a 75%,#3f7d1f 100%)}
.hero-title{left:0;top:300px;width:1200px;text-align:center;font-family:var(--display);font-size:70px;line-height:72px;color:#fff;text-shadow:0 2px 8px rgba(0,0,0,.35)}
.hero-sub{left:0;top:470px;width:1200px;text-align:center;font-size:21px;line-height:32px;color:#fff}
.btn{display:flex;align-items:center;justify-content:center;gap:6px;color:#fff;font-family:var(--text);font-weight:600;font-size:12.5px;letter-spacing:.3px}
.hero .b1{position:absolute;left:437px;top:467px;width:154px;height:44px;background:var(--bronze)}
.hero .b2{position:absolute;left:608px;top:467px;width:155px;height:44px;background:var(--green)}
.scroll{left:103px;top:225px;width:30px;height:420px}
.scroll span{position:absolute;left:-50px;top:300px;transform:rotate(-90deg);font-size:11px;color:#fff;letter-spacing:1px;white-space:nowrap}

/* headings */
.h2{width:1200px;left:0;text-align:center;font-family:var(--head);font-weight:700;font-size:35px;color:var(--ink);letter-spacing:.5px}
.h2.light{color:#fff}
.rule{left:560px;width:80px;height:4px;background:var(--green)}

/* who */
.who-text{left:240px;top:898px;width:720px;text-align:center;font-size:15.5px;line-height:29px;color:#333}
.feature{display:flex;align-items:center;gap:14px;font-weight:500;font-size:14px;line-height:21px;color:#222}

/* services diagram */
.services-band{left:0;top:1180px;width:1200px;height:715px;overflow:hidden}
.diagram-label{font-family:var(--head);font-weight:600;font-size:19px;color:#fff;letter-spacing:.3px}

/* gallery */
.tile{position:absolute}
.see-all{left:508px;top:2613px;width:182px;height:42px;background:var(--green)}

/* why */
.why-col{width:280px;text-align:center;color:#fff}
.why-col h3{font-family:var(--text);font-weight:600;font-size:16px;margin-top:0}
.why-col p{font-size:13.5px;line-height:21px;color:#c9cdcb;margin-top:11px}

/* testimonials */
.quote-card{position:absolute;top:3412px;width:310px;height:290px;padding:30px 32px}
.quote-card.active{background:#fff;box-shadow:0 4px 22px rgba(0,0,0,.12)}
.stars{color:#f5a300;font-size:21px;letter-spacing:2px;line-height:22px}
.quote-card h4{font-weight:500;font-size:14.5px;color:#222;margin-top:10px}
.quote-card p{font-size:13px;line-height:22.5px;color:#555;margin-top:12px}
.who{position:absolute;left:32px;bottom:32px;display:flex;gap:14px;align-items:center}
.avatar{width:34px;height:34px;border-radius:50%;background:linear-gradient(135deg,#9a9a9a,#3d3d3d)}
.who b{display:block;font-weight:600;font-size:13px;color:#222}
.who span{font-size:13px;color:#555}
.dots{left:568px;top:3733px;display:flex;gap:7px}
.dots i{width:9px;height:9px;border-radius:50%;border:1px solid #999}
.dots i.on{background:var(--green);border-color:var(--green)}

/* contact */
.contact{left:0;top:3820px;width:1200px;height:760px;background:var(--paper)}
.eyebrow{left:0;top:3879px;width:1200px;text-align:center;color:var(--green);font-weight:500;font-size:15px}
.field{position:absolute;background:var(--field);padding:0 22px;font-size:13px;font-style:italic;color:#999;display:flex;align-items:center}
.send{left:478px;top:4355px;width:245px;height:47px;background:var(--green);border-radius:24px;font-size:16px;font-weight:500}

/* footer */
.footer-bg{left:0;top:4470px;width:1200px;height:581px}
.cta-text{left:217px;top:4614px;font-size:19px;color:#fff}
.cta-btn{left:878px;top:4609px;width:154px;height:38px;background:var(--green);font-size:11.5px}
.f-title{font-size:16.5px;color:#fff;font-weight:500}
.f-bar{width:30px;height:2px;background:var(--green)}
.f-links{font-size:13px;line-height:23.5px;color:#e6e6e6}
.f-item{display:flex;gap:10px;font-size:12.5px;line-height:19px;color:#e6e6e6}
.f-social{width:22px;height:22px;border-radius:50%;background:var(--green)}
.f-small{font-size:12px;color:#cfd3d1}
</style>
</head>
<body>

<!-- Top bar -->
<div class="abs topbar">
  <span class="social" style="left:98px"></span>
  <span class="social" style="left:134px"></span>
  <span class="social" style="left:170px"></span>
  <div class="phone">
    <svg width="13" height="13" viewBox="0 0 24 24" fill="#fff"><path d="M6.6 10.8a15.1 15.1 0 0 0 6.6 6.6l2.2-2.2a1 1 0 0 1 1-.25 11.4 11.4 0 0 0 3.6.57 1 1 0 0 1 1 1V20a1 1 0 0 1-1 1A17 17 0 0 1 3 4a1 1 0 0 1 1-1h3.5a1 1 0 0 1 1 1c0 1.25.2 2.45.57 3.57a1 1 0 0 1-.25 1z"/></svg>
    +1 555 010 2040
  </div>
  <div class="mail">
    <svg width="13" height="11" viewBox="0 0 24 18" fill="#fff"><path d="M0 0h24v18H0z" fill="none"/><path d="M1 1h22v16H1z" fill="#fff"/><path d="M1 1l11 8 11-8" stroke="#2b3330" stroke-width="2" fill="none"/></svg>
    info@harrowmere.com
  </div>
</div>

<!-- Navigation -->
<nav class="abs nav">
  <a class="active" style="left:102px">Home</a>
  <span class="sep" style="left:169px"></span>
  <a style="left:191px">About Us</a>
  <span class="sep" style="left:280px"></span>
  <a style="left:304px">Services</a>
  <a style="left:773px">Projects</a>
  <span class="sep" style="left:853px"></span>
  <a style="left:876px">Contact</a>
  <a class="quote">
    <svg width="16" height="16" viewBox="0 0 24 24" fill="none" stroke="#fff" stroke-width="2"><path d="M11 4H4v16h16v-7"/><path d="M18 2l4 4-10 10H8v-4z"/></svg>
    Get A Quote
  </a>
</nav>
<div class="abs brand-badge"><span class="brand-dot"></span><span class="brand-name">HARROWMERE</span></div>

<!-- Hero -->
<header class="abs hero" role="img" aria-label="Photo of a two-storey grey family home with a wide green lawn under a blue sky">
  <div class="abs scroll">
    <svg width="30" height="420" viewBox="0 0 30 420"><circle cx="8" cy="12" r="7" fill="none" stroke="#fff" stroke-width="1.5"/><line x1="8" y1="19" x2="8" y2="220" stroke="#fff" stroke-width="1"/><line x1="8" y1="340" x2="8" y2="420" stroke="#fff"/><circle cx="8" cy="400" r="4" fill="var(--bronze)"/></svg>
    <span>SCROLL DOWN</span>
  </div>
  <a class="btn b1">LANDSCAPING <svg width="11" height="10" viewBox="0 0 12 10"><path d="M0 5h10M6 1l4 4-4 4" stroke="#fff" stroke-width="1.8" fill="none"/></svg></a>
  <a class="btn b2">CONSTRUCTION <svg width="11" height="10" viewBox="0 0 12 10"><path d="M0 5h10M6 1l4 4-4 4" stroke="#fff" stroke-width="1.8" fill="none"/></svg></a>
</header>
<h1 class="abs hero-title">Make Home<br>Amazing</h1>
<p class="abs hero-sub">What type of services are you<br>interested in ?</p>
<svg class="abs" style="left:0;top:660px" width="1200" height="145" viewBox="0 660 1200 145">
  <polygon points="0,770 600,677 1200,770 1200,805 0,805" fill="var(--green-light)"/>
  <polygon points="0,778 600,690 1200,778 1200,805 0,805" fill="#fff"/>
</svg>

<!-- Who we are -->
<h2 class="abs h2" style="top:843px">WHO WE ARE</h2>
<p class="abs who-text">Lorem Ipsum is simply dummy text of the printing and typesetting industry. Lorem Ipsum has been the industry's standard dummy text ever since the 1500s,</p>

<div class="abs feature" style="left:157px;top:1011px">
  <svg width="72" height="76" viewBox="0 0 72 76"><polygon points="36,2 68,20 68,56 36,74 4,56 4,20" fill="var(--green)"/><circle cx="36" cy="30" r="8" fill="none" stroke="#fff" stroke-width="2.5"/><path d="M22 52l8-6h12l8 6" fill="none" stroke="#fff" stroke-width="2.5"/></svg>
  <span>We've Repution For<br>Excellence</span>
</div>
<div class="abs feature" style="left:421px;top:1011px">
  <svg width="72" height="76" viewBox="0 0 72 76"><polygon points="36,2 68,20 68,56 36,74 4,56 4,20" fill="var(--green)"/><path d="M18 36l10-8 8 6 8-6 10 8-12 12-6-4-6 4z" fill="none" stroke="#fff" stroke-width="2.5"/></svg>
  <span>We Build<br>Partnerships</span>
</div>
<div class="abs feature" style="left:643px;top:1011px">
  <svg width="72" height="76" viewBox="0 0 72 76"><polygon points="36,2 68,20 68,56 36,74 4,56 4,20" fill="var(--green)"/><circle cx="26" cy="30" r="5" fill="none" stroke="#fff" stroke-width="2.5"/><circle cx="46" cy="30" r="5" fill="none" stroke="#fff" stroke-width="2.5"/><path d="M18 52v-8h16v8M38 52v-8h16v8" fill="none" stroke="#fff" stroke-width="2.5"/></svg>
  <span>Guided By<br>Commitment</span>
</div>
<div class="abs feature" style="left:863px;top:1011px">
  <svg width="72" height="76" viewBox="0 0 72 76"><polygon points="36,2 68,20 68,56 36,74 4,56 4,20" fill="var(--green)"/><circle cx="24" cy="30" r="4.5" fill="none" stroke="#fff" stroke-width="2.5"/><circle cx="36" cy="26" r="4.5" fill="none" stroke="#fff" stroke-width="2.5"/><circle cx="48" cy="30" r="4.5" fill="none" stroke="#fff" stroke-width="2.5"/><path d="M16 52v-10h12M30 52V38h12v14M44 42h12v10" fill="none" stroke="#fff" stroke-width="2.5"/></svg>
  <span>A Team Of<br>Professionals</span>
</div>

<!-- Services diagram band -->
<section class="abs services-band">
  <svg width="1200" height="715" viewBox="0 1180 1200 715">
    <defs>
      <linearGradient id="bandFill" x1="0" y1="0" x2="0" y2="1">
        <stop offset="0" stop-color="#0d8a2b"/>
        <stop offset="1" stop-color="#075e1c"/>
      </linearGradient>
    </defs>
    <polygon points="0,1280 600,1192 1200,1280 1200,1895 0,1895" fill="var(--green-light)"/>
    <polygon role="img" aria-label="Green-tinted photo of a house roofline" points="0,1298 600,1212 1200,1298 1200,1895 0,1895" fill="url(#bandFill)"/>
    <circle cx="600" cy="1773" r="255" fill="none" stroke="#bdbdbd" stroke-width="9"/>
    <g stroke="var(--green-light)" stroke-width="3" fill="none">
      <polyline points="290,1467 460,1467 498,1508"/>
      <polyline points="910,1467 740,1467 702,1508"/>
      <polyline points="172,1567 355,1567 380,1605"/>
      <polyline points="1028,1567 845,1567 820,1605"/>
      <polyline points="124,1708 296,1708 322,1742"/>
      <polyline points="1076,1708 904,1708 878,1742"/>
    </g>
    <g stroke="#fff" stroke-width="4" fill="#2f3833">
      <polygon points="345,1726 381,1746 381,1788 345,1808 309,1788 309,1746"/>
      <polygon points="400,1589 436,1609 436,1651 400,1671 364,1651 364,1609"/>
      <polygon points="518,1490 554,1510 554,1552 518,1572 482,1552 482,1510"/>
      <polygon points="684,1490 720,1510 720,1552 684,1572 648,1552 648,1510"/>
      <polygon points="800,1589 836,1609 836,1651 800,1671 764,1651 764,1609"/>
      <polygon points="855,1726 891,1746 891,1788 855,1808 819,1788 819,1746"/>
    </g>
    <g stroke="#fff" stroke-width="2.5" fill="none">
      <!-- building -->
      <path d="M333 1785v-28h14v28M347 1764h10v21M337 1764h6M337 1772h6"/>
      <!-- landscaping -->
      <path d="M394 1648v-10M392 1628c-6 8-6 14 2 16 8-2 8-8 2-16zM408 1648v-8M406 1632c-5 6-4 10 2 12 6-2 6-6 0-12z"/>
      <!-- decking -->
      <path d="M500 1528l18-14 18 14M506 1530v18M530 1530v18M512 1536v12M518 1536v12M524 1536v12"/>
      <!-- maintenance -->
      <path d="M670 1517l28 28M698 1517l-28 28M664 1521l6-6M698 1545l6-6"/>
      <!-- roofing -->
      <path d="M782 1644l18-18 18 18M786 1648h28M790 1640l10-10 10 10"/>
      <!-- gutters -->
      <path d="M838 1762h30v8h-30zM852 1770v14M846 1788l-4 6M856 1788v6M866 1786l3 6M842 1758l4-6M862 1756l3-5"/>
    </g>
    <polygon points="0,1895 600,1824 1200,1895" fill="#fff"/>
  </svg>
  <h2 class="abs h2 light" style="top:135px">OUR SERVICES</h2>
  <svg class="abs" style="left:518px;top:193px" width="164" height="14" viewBox="0 0 164 14"><line x1="0" y1="7" x2="62" y2="7" stroke="#b7d9b3" stroke-width="1.5"/><line x1="102" y1="7" x2="164" y2="7" stroke="#b7d9b3" stroke-width="1.5"/><circle cx="70" cy="7" r="4" fill="var(--green-light)"/><circle cx="82" cy="7" r="6" fill="var(--green-light)"/><circle cx="94" cy="7" r="4" fill="var(--green-light)"/></svg>
  <span class="abs diagram-label" style="left:300px;top:257px">DECKING</span>
  <span class="abs diagram-label" style="left:764px;top:257px">MAINTENANCE</span>
  <span class="abs diagram-label" style="left:182px;top:357px">LANDSCAPING</span>
  <span class="abs diagram-label" style="left:927px;top:357px">ROOFING</span>
  <span class="abs diagram-label" style="left:129px;top:494px">BUILDING</span>
  <span class="abs diagram-label" style="left:981px;top:494px">GUTTERS</span>
</section>

<!-- Project gallery -->
<h2 class="abs h2" style="top:1938px">OUR SERVICES</h2>
<div class="abs rule" style="top:1992px"></div>
<div class="tile" style="left:163px;top:2026px;width:435px;height:251px;background:linear-gradient(160deg,#cfc9bc 0%,#b6aa96 55%,#5b6f8e 100%)" role="img" aria-label="Photo of a modern school building with glass facade"></div>
<div class="tile" style="left:603px;top:2026px;width:434px;height:251px;background:linear-gradient(180deg,#7c7ea8 0%,#b99c8a 40%,#56555a 70%,#4c6b36 100%)" role="img" aria-label="Photo of a suburban home at dusk with warm lit windows"></div>
<div class="tile" style="left:163px;top:2285px;width:292px;height:268px;background:linear-gradient(180deg,#2f6fd1 0%,#6b94d8 35%,#8a4a3e 60%,#4d5a3c 100%)" role="img" aria-label="Photo of a red brick family home under blue sky"></div>
<div class="tile" style="left:460px;top:2285px;width:283px;height:268px;background:linear-gradient(180deg,#8cc5c8 0%,#c9b84a 40%,#3e8a2e 70%,#2f78a0 100%)" role="img" aria-label="Photo of a yellow villa with gardens and a pond"></div>
<div class="tile" style="left:748px;top:2285px;width:289px;height:268px;background:linear-gradient(180deg,#4f8ad8 0%,#a9c2e0 30%,#6d7470 60%,#3d6b2e 100%)" role="img" aria-label="Photo of a grey craftsman-style house with shrubs"></div>
<a class="abs btn see-all">SEE ALL PROJECTS <svg width="11" height="10" viewBox="0 0 12 10"><path d="M0 5h10M6 1l4 4-4 4" stroke="#fff" stroke-width="1.8" fill="none"/></svg></a>

<!-- Why choose us -->
<svg class="abs" style="left:0;top:2715px" width="1200" height="540" viewBox="0 2715 1200 540">
  <polygon points="0,2800 600,2722 1200,2800 1200,3250 0,3250" fill="var(--bronze)"/>
  <polygon points="0,2810 600,2736 1200,2810 1200,3250 0,3250" fill="var(--charcoal)"/>
</svg>
<h2 class="abs h2 light" style="top:2822px">WHY CHOOSE US</h2>
<svg class="abs" style="left:518px;top:2880px" width="164" height="14" viewBox="0 0 164 14"><line x1="0" y1="7" x2="62" y2="7" stroke="#7a7f7c" stroke-width="1.5"/><line x1="102" y1="7" x2="164" y2="7" stroke="#7a7f7c" stroke-width="1.5"/><circle cx="70" cy="7" r="4" fill="var(--bronze)"/><circle cx="82" cy="7" r="6" fill="var(--bronze)"/><circle cx="94" cy="7" r="4" fill="var(--bronze)"/></svg>

<div class="abs why-col" style="left:176px;top:2942px">
  <svg width="82" height="92" viewBox="0 0 82 92"><polygon points="41,2 79,24 79,68 41,90 3,68 3,24" fill="var(--bronze)"/><polygon points="41,12 70,29 70,63 41,80 12,63 12,29" fill="#2f3632"/><path d="M29 62V36h14v26zM43 44h10v18zM33 41h6M33 48h6M33 55h6" stroke="var(--bronze)" stroke-width="3" fill="none"/></svg>
  <h3 style="margin-top:22px">HIGH QUALITY WORK</h3>
  <p>Lorem Ipsum is simply dummy<br>text of the printing and typeset-<br>ting industry standard</p>
</div>
<div class="abs why-col" style="left:454px;top:2942px">
  <svg width="82" height="92" viewBox="0 0 82 92"><polygon points="41,2 79,24 79,68 41,90 3,68 3,24" fill="var(--bronze)"/><polygon points="41,12 70,29 70,63 41,80 12,63 12,29" fill="#2f3632"/><path d="M29 62V36h14v26zM43 44h10v18zM33 41h6M33 48h6M33 55h6" stroke="var(--bronze)" stroke-width="3" fill="none"/></svg>
  <h3 style="margin-top:22px">PROFESSIONAL TEAM</h3>
  <p>Lorem Ipsum is simply dummy<br>text of the printing and typeset-<br>ting industry standard</p>
</div>
<div class="abs why-col" style="left:744px;top:2942px">
  <svg width="82" height="92" viewBox="0 0 82 92"><polygon points="41,2 79,24 79,68 41,90 3,68 3,24" fill="var(--bronze)"/><polygon points="41,12 70,29 70,63 41,80 12,63 12,29" fill="#2f3632"/><path d="M29 62V36h14v26zM43 44h10v18zM33 41h6M33 48h6M33 55h6" stroke="var(--bronze)" stroke-width="3" fill="none"/></svg>
  <h3 style="margin-top:22px">YEARS OF EXPERIENCE</h3>
  <p>Lorem Ipsum is simply dummy<br>text of the printing and typeset-<br>ting industry standard</p>
</div>

<!-- Testimonials -->
<h2 class="abs h2" style="top:3318px">TESTIMONIALS</h2>
<div class="abs rule" style="top:3372px"></div>

<div class="quote-card" style="left:117px">
  <div class="stars">★★★★★</div>
  <h4>"SOLID Service! Vety consistent!"</h4>
  <p>the printing and typesetting industry. Lorem Ipsum has been the industry's standard dummy text ever since the 1500s Lorem Ipsum!</p>
  <div class="who"><span class="avatar" role="img" aria-label="Client portrait"></span><div><b>Marlo Fenwick</b><span>Web Development</span></div></div>
</div>
<div class="quote-card active" style="left:445px">
  <div class="stars">★★★★★</div>
  <h4>"SOLID Service! Vety consistent!"</h4>
  <p>the printing and typesetting industry. Lorem Ipsum has been the industry's standard dummy text ever since the 1500s Lorem Ipsum!</p>
  <div class="who"><span class="avatar" role="img" aria-label="Client portrait"></span><div><b>Marlo Fenwick</b><span>Web Development</span></div></div>
</div>
<div class="quote-card" style="left:778px">
  <div class="stars">★★★★★</div>
  <h4>"SOLID Service! Vety consistent!"</h4>
  <p>the printing and typesetting industry. Lorem Ipsum has been the industry's standard dummy text ever since the 1500s Lorem Ipsum!</p>
  <div class="who"><span class="avatar" role="img" aria-label="Client portrait"></span><div><b>Marlo Fenwick</b><span>Web Development</span></div></div>
</div>
<div class="abs dots"><i></i><i class="on"></i><i></i><i></i></div>

<!-- Contact -->
<section class="abs contact"></section>
<p class="abs eyebrow">CONTACT US</p>
<h2 class="abs h2" style="top:3910px">LET’S DO SOMETING GREAT TOGETHER</h2>
<p class="abs" style="left:0;top:3974px;width:1200px;text-align:center;font-size:15.5px;color:#444">Fill up the form and our team will get back to you within 24 hours</p>
<div class="field" style="left:157px;top:4034px;width:437px;height:61px">First Name</div>
<div class="field" style="left:602px;top:4034px;width:437px;height:61px">Last Name</div>
<div class="field" style="left:157px;top:4101px;width:437px;height:57px">Email Address</div>
<div class="field" style="left:602px;top:4101px;width:437px;height:57px">Phone Number</div>
<div class="field" style="left:157px;top:4170px;width:882px;height:144px;align-items:flex-start;padding-top:22px">Type you Message here!</div>
<a class="abs btn send">SEND US MESSAGE</a>

<!-- Footer -->
<svg class="abs footer-bg" width="1200" height="581" viewBox="0 4470 1200 581">
  <polygon points="0,4552 600,4477 1200,4552 1200,5051 0,5051" fill="var(--bronze)"/>
  <polygon points="0,4562 600,4490 1200,4562 1200,5051 0,5051" fill="var(--charcoal)"/>
  <line x1="0" y1="4686" x2="1200" y2="4686" stroke="#414a46"/>
  <line x1="378" y1="4730" x2="378" y2="4930" stroke="#414a46"/>
  <line x1="563" y1="4730" x2="563" y2="4930" stroke="#414a46"/>
  <line x1="866" y1="4730" x2="866" y2="4930" stroke="#414a46"/>
  <line x1="912" y1="4836" x2="1080" y2="4836" stroke="#414a46"/>
  <line x1="170" y1="4964" x2="1040" y2="4964" stroke="#414a46"/>
</svg>
<p class="abs cta-text">Have any question or <b style="font-weight:600">need any business consultation?</b></p>
<a class="abs btn cta-btn">CONTACT US NOW!!</a>

<div class="abs" style="left:200px;top:4740px;width:110px;height:70px;background:#fff;border-radius:8px 8px 40px 40px;display:flex;align-items:center;justify-content:center"><span class="brand-name" style="font-size:12px">HARROWMERE</span></div>
<p class="abs f-small" style="left:171px;top:4836px;width:180px;font-size:11px;line-height:19px">Lorem ipsum dolor sit amet, con-sectetur adipiscing elit. Nullam sollicitudin tempor sem vitae pre-tium. Fusce ultricies</p>

<div class="abs f-bar" style="left:439px;top:4722px"></div>
<p class="abs f-title" style="left:439px;top:4739px">Site Links</p>
<p class="abs f-links" style="left:439px;top:4781px">Home<br>About Us<br>Services<br>Rotes<br>Contact Us</p>

<div class="abs f-bar" style="left:614px;top:4722px"></div>
<p class="abs f-title" style="left:614px;top:4739px">Contact Us</p>
<div class="abs f-item" style="left:614px;top:4765px">
  <svg width="14" height="14" viewBox="0 0 24 24" fill="none" stroke="#fff" stroke-width="1.8"><path d="M6.6 10.8a15.1 15.1 0 0 0 6.6 6.6l2.2-2.2 4.6 1.6V21A17 17 0 0 1 3 4h4.8l1.6 4.6z"/></svg>
  <span>Phone: 555 010 2041</span>
</div>
<div class="abs f-item" style="left:614px;top:4812px;width:210px">
  <svg width="14" height="16" viewBox="0 0 24 28" fill="none" stroke="#fff" stroke-width="2" style="flex:none"><path d="M12 26s9-9 9-15a9 9 0 0 0-18 0c0 6 9 15 9 15z"/><circle cx="12" cy="11" r="3"/></svg>
  <span>Address: 48 Elm Row, Suite 2, Brookfield Lane, Millbrook, MB</span>
</div>
<div class="abs f-item" style="left:614px;top:4888px">
  <svg width="15" height="13" viewBox="0 0 24 20" fill="none" stroke="#fff" stroke-width="2"><path d="M2 2h20v16H2z"/><path d="M2 2l10 8 10-8"/></svg>
  <span>Email: hello@harrowmere.com</span>
</div>

<div class="abs f-bar" style="left:912px;top:4722px"></div>
<p class="abs f-title" style="left:912px;top:4739px">Get Connected</p>
<div class="abs" style="left:912px;top:4776px;display:flex;gap:7px"><span class="f-social"></span><span class="f-social"></span><span class="f-social"></span></div>
<div class="abs f-bar" style="left:912px;top:4842px"></div>
<p class="abs f-title" style="left:912px;top:4852px">Newsletter</p>
<div class="abs" style="left:912px;top:4895px;width:130px;height:30px;background:#fff;font-size:10px;color:#888;padding:8px 8px">Email..</div>
<div class="abs" style="left:1042px;top:4895px;width:32px;height:30px;background:var(--green);display:flex;align-items:center;justify-content:center">
  <svg width="14" height="14" viewBox="0 0 24 24" fill="#fff"><path d="M2 11L22 2l-9 20-2-8z"/></svg>
</div>

<p class="abs f-small" style="left:186px;top:4989px">@2024 Harrowmere &nbsp;|&nbsp; All Rights Reserved.</p>
<p class="abs f-small" style="right:163px;top:4989px">Terms &amp; Conditions &nbsp;|&nbsp; Privacy Policy</p>

</body>
</html>
```